A Leisure SPA Plaza Hotel needs Creative VIP Cards Design

We need VIP Cards Design for a SPA Plaza Hotel, This leisure SPA plaza hotel have multiple sub projects, such as leisure hotel room, large buffet restaurant, swimming pool, theatrical performances, sauna bath, massage, SPA, Tea bar, 3D cinema, KTV rooms, chess room, Internet cafes , art appreciation, children's Castle, Korean geothermal, table tennis, billiard room, GYM and other entertainments.
We need Three creative VIP Card design for 3 different level:
1. Golden Card
2. Platinum Card
3. Diamond Card
Attached, Please find the LOGO file and some sample, we new design with much better look than those samples.

```html
<!DOCTYPE html>
<html lang="en">
<head>
<meta charset="utf-8">
<title>Bayview Leisure Plaza — VIP Cards</title>
<link rel="stylesheet" href="https://fonts.googleapis.com/css2?family=Libre+Baskerville:wght@400;700&display=swap">
<style>
  :root {
    --bg: #000000;
    --label: #ffffff;
    --band: #ffffff;
    --band-soft: #f1f1f3;
    --vip-ink: #454545;
    --brand-ink: #1f9bbf;
    --brand-dot: #f4b942;
    --gold-top: #c49536;
    --gold-mid: #c6bb4c;
    --gold-low: #e8c25a;
    --gold-bottom: #f4ad45;
    --gold-ink: #3b2812;
    --gold-ornament: 90, 58, 28;
    --gold-swirl: 150, 110, 40;
    --plat-top: #3d3d3d;
    --plat-mid: #d8d8d8;
    --plat-low: #9a9a9a;
    --plat-bottom: #444444;
    --plat-swirl: 90, 90, 90;
    --dia-top: #7b93a3;
    --dia-mid: #2585b4;
    --dia-bottom: #1c3f98;
    --dia-swirl: 180, 220, 240;
    --light-ornament: 255, 255, 255;
  }
  * { box-sizing: border-box; margin: 0; padding: 0; }
  html, body {
    width: 1200px; height: 1200px; overflow: hidden; background: var(--bg);
  }
  .canvas {
    position: relative; width: 1000px; height: 1000px;
    transform: scale(1.2); transform-origin: 0 0;
    font-family: "Libre Baskerville", Georgia, serif;
  }
  .tier-label {
    position: absolute; color: var(--label); font-weight: 700;
    font-size: 36px; letter-spacing: 1px; line-height: 1;
  }
  .tier-label--gold { left: 80px; top: 166px; }
  .tier-label--platinum { left: 192px; top: 484px; width: 240px; text-align: center; }
  .tier-label--diamond { left: 568px; top: 481px; }

  .card {
    position: absolute; width: 250px; height: 418px; border-radius: 22px; overflow: hidden;
  }
  .card::after {
    content: ""; position: absolute; inset: 0; pointer-events: none; z-index: 1;
    background: repeating-linear-gradient(45deg,
      rgba(255,255,255,0) 0 34px, rgba(255,255,255,0.14) 34px 62px);
  }
  .card--gold { background: linear-gradient(180deg, var(--gold-top) 0%, var(--gold-mid) 45%, var(--gold-low) 75%, var(--gold-bottom) 100%); }
  .card--platinum { background: linear-gradient(180deg, var(--plat-top) 0%, var(--plat-low) 25%, var(--plat-mid) 55%, var(--plat-low) 78%, var(--plat-bottom) 100%); }
  .card--diamond { background: linear-gradient(180deg, var(--dia-top) 0%, var(--dia-mid) 50%, var(--dia-bottom) 100%); }

  .card--gold-front { left: 230px; top: 42px; }
  .card--gold-back { left: 498px; top: 42px; }
  .card--platinum-front { left: 192px; top: 543px; }
  .card--diamond-front { left: 540px; top: 543px; }

  /* soft tonal field where the floral swirls sit */
  .swirl-field {
    position: absolute; inset: 0; z-index: 0; pointer-events: none;
  }
  .card--gold .swirl-field {
    background:
      radial-gradient(ellipse 90px 120px at 200px 250px, rgba(var(--gold-swirl), 0.35), transparent 70%),
      radial-gradient(ellipse 70px 90px at 40px 380px, rgba(var(--gold-swirl), 0.25), transparent 70%);
  }
  .card--gold-back .swirl-field {
    background:
      radial-gradient(ellipse 110px 150px at 90px 200px, rgba(var(--gold-swirl), 0.35), transparent 70%),
      radial-gradient(ellipse 90px 120px at 200px 260px, rgba(var(--gold-swirl), 0.3), transparent 70%),
      radial-gradient(ellipse 70px 80px at 210px 380px, rgba(var(--gold-swirl), 0.25), transparent 70%);
  }
  .card--platinum .swirl-field {
    background:
      radial-gradient(ellipse 80px 110px at 30px 170px, rgba(var(--plat-swirl), 0.35), transparent 70%),
      radial-gradient(ellipse 90px 120px at 220px 210px, rgba(var(--plat-swirl), 0.3), transparent 70%);
  }
  .card--diamond .swirl-field {
    background:
      radial-gradient(ellipse 80px 120px at 30px 190px, rgba(var(--dia-swirl), 0.3), transparent 70%),
      radial-gradient(ellipse 90px 130px at 225px 180px, rgba(var(--dia-swirl), 0.3), transparent 70%),
      radial-gradient(ellipse 70px 60px at 220px 400px, rgba(var(--dia-swirl), 0.2), transparent 70%);
  }

  /* scroll flourish areas: soft band fading toward both ends */
  .ornament {
    position: absolute; left: 50%; width: 170px; height: 28px; transform: translateX(-50%);
    z-index: 2;
  }
  .ornament--top { top: 16px; }
  .ornament--bottom { top: 370px; }
  .ornament--dark {
    background:
      radial-gradient(ellipse 30px 14px at 50% 50%, rgba(var(--gold-ornament), 0.75), transparent 100%),
      linear-gradient(90deg, transparent 0%, rgba(var(--gold-ornament), 0.45) 25%, rgba(var(--gold-ornament), 0.55) 50%, rgba(var(--gold-ornament), 0.45) 75%, transparent 100%);
  }
  .ornament--light {
    background:
      radial-gradient(ellipse 30px 14px at 50% 50%, rgba(var(--light-ornament), 0.8), transparent 100%),
      linear-gradient(90deg, transparent 0%, rgba(var(--light-ornament), 0.45) 25%, rgba(var(--light-ornament), 0.55) 50%, rgba(var(--light-ornament), 0.45) 75%, transparent 100%);
  }
  .ornament--top { -webkit-mask: linear-gradient(180deg, #000 0 70%, transparent 100%); mask: linear-gradient(180deg, #000 0 70%, transparent 100%); }
  .ornament--bottom { -webkit-mask: linear-gradient(0deg, #000 0 70%, transparent 100%); mask: linear-gradient(0deg, #000 0 70%, transparent 100%); }

  .brand-panel {
    position: absolute; left: 38px; top: 69px; width: 182px; height: 116px;
    background: var(--band); display: flex; align-items: center; justify-content: center;
    gap: 8px; z-index: 2; padding: 0 10px;
  }
  .brand-dot { width: 20px; height: 20px; border-radius: 50%; background: var(--brand-dot); flex: none; }
  .brand-name {
    color: var(--brand-ink); font-weight: 400; font-size: 15px; line-height: 1.3;
  }

  .vip-band {
    position: absolute; left: 0; top: 249px; width: 100%; height: 88px;
    background: var(--band); z-index: 2;
    display: flex; align-items: center; justify-content: center;
  }
  .card--platinum .vip-band, .card--diamond .vip-band { background: var(--band-soft); }
  .vip-mark { color: var(--vip-ink); font-size: 74px; font-weight: 400; line-height: 1; padding-top: 8px; }

  .member-no {
    position: absolute; left: 0; top: 342px; width: 100%; text-align: center;
    font-weight: 700; font-size: 22px; line-height: 1.2; z-index: 3;
  }
  .card--gold .member-no { color: var(--gold-ink); }
  .card--platinum .member-no, .card--diamond .member-no { color: var(--label); }

  .terms-title {
    position: absolute; top: 97px; width: 100%; text-align: center;
    font-weight: 700; font-size: 13px; color: var(--gold-ink); z-index: 2;
  }
  .signature-label {
    position: absolute; left: 22px; top: 280px; font-weight: 700; font-size: 16px;
    color: var(--gold-ink); z-index: 2;
  }
  .signature-box {
    position: absolute; left: 21px; top: 308px; width: 206px; height: 34px;
    background: var(--band); border: 2px solid var(--gold-ink); z-index: 2;
  }
</style>
</head>
<body>
<main class="canvas">
  <h2 class="tier-label tier-label--gold">GOLD</h2>
  <h2 class="tier-label tier-label--platinum">PLATINUM</h2>
  <h2 class="tier-label tier-label--diamond">DIAMOND</h2>

  <section class="card card--gold card--gold-front" aria-label="Gold VIP card, front">
    <div class="swirl-field" role="img" aria-label="Faint floral swirl pattern"></div>
    <div class="ornament ornament--top ornament--dark" role="img" aria-label="Scrollwork flourish"></div>
    <div class="brand-panel"><span class="brand-dot"></span><span class="brand-name">Bayview Leisure Plaza</span></div>
    <div class="vip-band"><span class="vip-mark">VIP</span></div>
    <p class="member-no">NO. 000001</p>
    <div class="ornament ornament--bottom ornament--dark" role="img" aria-label="Scrollwork flourish"></div>
  </section>

  <section class="card card--gold card--gold-back" aria-label="Gold VIP card, back">
    <div class="swirl-field" role="img" aria-label="Faint floral swirl pattern"></div>
    <div class="ornament ornament--top ornament--dark" role="img" aria-label="Scrollwork flourish"></div>
    <p class="terms-title">Terms &amp; Condition</p>
    <p class="signature-label">Authorized Signature</p>
    <div class="signature-box"></div>
    <div class="ornament ornament--bottom ornament--dark" role="img" aria-label="Scrollwork flourish"></div>
  </section>

  <section class="card card--platinum card--platinum-front" aria-label="Platinum VIP card, front">
    <div class="swirl-field" role="img" aria-label="Faint floral swirl pattern"></div>
    <div class="ornament ornament--top ornament--light" role="img" aria-label="Scrollwork flourish"></div>
    <div class="brand-panel"><span class="brand-dot"></span><span class="brand-name">Bayview Leisure Plaza</span></div>
    <div class="vip-band"><span class="vip-mark">VIP</span></div>
    <p class="member-no">NO. 000001</p>
    <div class="ornament ornament--bottom ornament--light" role="img" aria-label="Scrollwork flourish"></div>
  </section>

  <section class="card card--diamond card--diamond-front" aria-label="Diamond VIP card, front">
    <div class="swirl-field" role="img" aria-label="Faint floral swirl pattern"></div>
    <div class="ornament ornament--top ornament--light" role="img" aria-label="Scrollwork flourish"></div>
    <div class="brand-panel"><span class="brand-dot"></span><span class="brand-name">Bayview Leisure Plaza</span></div>
    <div class="vip-band"><span class="vip-mark">VIP</span></div>
    <p class="member-no">NO. 000001</p>
    <div class="ornament ornament--bottom ornament--light" role="img" aria-label="Scrollwork flourish"></div>
  </section>
</main>
</body>
</html>
```